Business Card, Stationary, & Folder for Mortgage Company
KLD Mortgage
Business Card, Stationary, & Folder for Mortgage Company - Real Estate
Creative Brief
Professional
Terrin Balk
Senior Loan Officer
4186 Orchard Crest Blvd, #209 Fairbrook Heights, Ohio 45999
tbalk@kldmortgage-example.com
www.KLDMortgage-example.com
I would like to use the colors in the logo but would like to also add a touch of red. I also would like to use the symbols for the phone numbers, email, and website
KLDMortgage KLDMortgage
I am looking for just a touch of red in the design. The main design should match the colors of the logo. Please don't alter the logo.
PixelHarborLab PixelHarborLab

```html
<!DOCTYPE html>
<html lang="en">
<head>
<meta charset="utf-8">
<title>KLD Mortgage – Business Card</title>
<link href="https://fonts.googleapis.com/css2?family=Open+Sans:wght@400;600;700&display=swap" rel="stylesheet">
<style>
:root{
  --stage:#2a2a2c;
  --card-white:#ffffff;
  --brand-blue:#2f63b8;
  --brand-blue-light:#6f9be0;
  --brand-navy:#1d3f7d;
  --ink:#3b3b3b;
  --ink-soft:#6a6a6a;
  --accent-red:#c8262c;
}
*{margin:0;padding:0;box-sizing:border-box}
html,body{width:1200px;height:698px;overflow:hidden;background:var(--stage);font-family:"Open Sans",Arial,sans-serif}
.stage{position:relative;width:1200px;height:698px}
.card{position:absolute;width:500px;height:286px;border-radius:14px;overflow:hidden;top:206px}
.card-front{left:70px;background:var(--card-white)}
.card-back{left:630px;background:radial-gradient(circle at 50% 40%,var(--brand-blue-light) 0%,var(--brand-blue) 55%,var(--brand-navy) 100%)}

.front-brand{position:absolute;right:34px;top:30px;display:flex;align-items:center;gap:10px}
.brand-dot{width:34px;height:34px;border-radius:50%;background:var(--brand-blue)}
.brand-name{font-weight:700;font-size:26px;color:var(--brand-blue);letter-spacing:.5px}

.person{position:absolute;left:30px;top:138px}
.person-name{font-size:22px;font-weight:600;color:var(--brand-blue)}
.person-title{font-size:12px;color:var(--ink-soft);margin-top:1px}
.address{font-size:11.5px;color:var(--ink);margin-top:10px;line-height:1.35}

.contact-list{list-style:none;font-size:11px;color:var(--ink);line-height:1.5}
.contact-list li{display:flex;align-items:center;gap:6px}
.contact-list svg{width:11px;height:11px;fill:var(--brand-blue);flex:none}
.contact-phones{position:absolute;left:30px;top:232px}
.contact-online{position:absolute;left:268px;top:148px}
.contact-online-phones{position:absolute;left:268px;top:214px}

.front-band{position:absolute;left:0;right:0;bottom:0;height:9px;background:var(--brand-blue)}
.front-band::after{content:"";position:absolute;right:0;top:0;width:70px;height:100%;background:var(--accent-red)}

.back-brand{position:absolute;left:0;right:0;top:0;bottom:0;display:flex;flex-direction:column;align-items:center;justify-content:center;gap:12px}
.back-brand .brand-dot{width:64px;height:64px;background:#ffffff}
.back-brand .brand-name{color:#ffffff;font-size:30px}
</style>
</head>
<body>
<main class="stage">
  <section class="card card-front" aria-label="Business card front">
    <div class="front-brand">
      <span class="brand-dot"></span>
      <span class="brand-name">KLD Mortgage</span>
    </div>

    <div class="person">
      <h1 class="person-name">Terrin Balk</h1>
      <p class="person-title">Senior Loan Officer</p>
      <p class="address">4186 Orchard Crest Blvd, #209<br>Fairbrook Heights, Ohio 45999</p>
    </div>

    <ul class="contact-list contact-phones">
      <li><svg viewBox="0 0 24 24"><path d="M6.6 10.8a15 15 0 0 0 6.6 6.6l2.2-2.2a1 1 0 0 1 1-.25 11.4 11.4 0 0 0 3.6.57 1 1 0 0 1 1 1V20a1 1 0 0 1-1 1A17 17 0 0 1 3 4a1 1 0 0 1 1-1h3.5a1 1 0 0 1 1 1c0 1.25.2 2.45.57 3.57a1 1 0 0 1-.25 1z"/></svg>T: 1-800-555-0142</li>
      <li><svg viewBox="0 0 24 24"><path d="M6.6 10.8a15 15 0 0 0 6.6 6.6l2.2-2.2a1 1 0 0 1 1-.25 11.4 11.4 0 0 0 3.6.57 1 1 0 0 1 1 1V20a1 1 0 0 1-1 1A17 17 0 0 1 3 4a1 1 0 0 1 1-1h3.5a1 1 0 0 1 1 1c0 1.25.2 2.45.57 3.57a1 1 0 0 1-.25 1z"/></svg>C: 301-555-0186</li>
    </ul>

    <ul class="contact-list contact-online">
      <li><svg viewBox="0 0 24 24"><path d="M2 5h20v14H2zm2 2v.5l8 5 8-5V7zm0 3v7h16v-7l-8 5z"/></svg>tbalk@kldmortgage-example.com</li>
      <li><svg viewBox="0 0 24 24"><path d="M12 2a10 10 0 1 0 0 20 10 10 0 0 0 0-20zm6.9 9h-3a15 15 0 0 0-1.3-5.6A8 8 0 0 1 18.9 11zM12 4.1c.9 1.3 1.8 3.6 1.9 6.9h-3.8c.1-3.3 1-5.6 1.9-6.9zM9.4 5.4A15 15 0 0 0 8.1 11h-3a8 8 0 0 1 4.3-5.6zM5.1 13h3a15 15 0 0 0 1.3 5.6A8 8 0 0 1 5.1 13zm6.9 6.9c-.9-1.3-1.8-3.6-1.9-6.9h3.8c-.1 3.3-1 5.6-1.9 6.9zm2.6-1.3a15 15 0 0 0 1.3-5.6h3a8 8 0 0 1-4.3 5.6z"/></svg>www.KLDMortgage-example.com</li>
    </ul>

    <ul class="contact-list contact-online-phones">
      <li><svg viewBox="0 0 24 24"><path d="M6.6 10.8a15 15 0 0 0 6.6 6.6l2.2-2.2a1 1 0 0 1 1-.25 11.4 11.4 0 0 0 3.6.57 1 1 0 0 1 1 1V20a1 1 0 0 1-1 1A17 17 0 0 1 3 4a1 1 0 0 1 1-1h3.5a1 1 0 0 1 1 1c0 1.25.2 2.45.57 3.57a1 1 0 0 1-.25 1z"/></svg>O: 301-555-0127</li>
      <li><svg viewBox="0 0 24 24"><path d="M4 7h16v10H4zM7 3h10v4H7zm0 14h10v4H7z"/></svg>F: 301-555-0163</li>
    </ul>

    <div class="front-band"></div>
  </section>

  <section class="card card-back" aria-label="Business card back">
    <div class="back-brand">
      <span class="brand-dot"></span>
      <span class="brand-name">KLD Mortgage</span>
    </div>
  </section>
</main>
</body>
</html>
```